Company selling food supplements with CBD needs label.

We need a label design for a company called "ULO Lab ltd", is based in the UK, the market name is "ULO" or "ULO Quiet Harvest Rituals". The initial product is Virgin Organic Hemp Seed Oil with a CBD in a 10ml amber dropper bottle. The design should be simplicity and luxury. The design should include also box.

Target Market(s)

Food supplements on Brivo UK

Industry/Entity Type

Supplement

Font styles to use
Other font styles liked:
• Some luxury

Colors

Designer to choose colors to be used in the design.

Requirements
Must have
• All the information on the label required by the UK for the food supplements, the same on the box. One version matt one transparent. The design should include different CBD content, one different bottle (250mg, 500mg, 750mg, 1000mg) .
• The label and box should include the following phrases: "DIRECTIONS: Food Supplement. Shake well before use. Use 4-6 drops 2-3 times a day. Leave the oil in your mouth for 30-60 seconds before swallowing. Gradually build up the dose to find your optimum dosage.
• CAUTION: Do not exceed the recommended daily intake. Do not use as a substitute for a varied diet. Do not use during pregnancy and breastfeeding. Store in a dark and cool place, away from sunlight. Keep away from children.
• INGREDIENTS: Hemp Seed Oil, Omega-6 (2800mg), Omega-3 (930mg), CBD (250mg)
• MANUFACTURED: ULO Lab Ltd, 58 Pembery Ln, Harrow, HA2 8LW, www,ulowerks.co.uk, info@ulowerks.co.uk.
• EXPIRED DATE: "
• The box should also include a place for bark code.
Nice to have
• Simple and elegant design vertical or horizontal with exposed company logo "ULO" or "ULO Quiet Harvest Rituals". The company logo is provided but designers may change it freely.
Should not have
• The best without pictures/graphics overloading simplicity and purity of design.

```html
<!DOCTYPE html>
<html lang="en">
<head>
<meta charset="utf-8">
<title>ULO Hemp Seed Oil Label</title>
<link rel="stylesheet" href="https://fonts.googleapis.com/css2?family=Bebas+Neue&family=Open+Sans:wght@400;600&display=swap">
<style>
  :root {
    --page-bg: #e2e2e2;
    --label-deep: #17463b;
    --label-mid: #25644f;
    --label-light: #3c8a6f;
    --leaf-tone: #4fa98a;
    --brand-green: #3fd17a;
    --ink-light: #f1f4f2;
    --ink-soft: #8fe0b8;
  }
  * { margin: 0; padding: 0; box-sizing: border-box; }
  html, body {
    width: 1200px;
    height: 900px;
    overflow: hidden;
    background: var(--page-bg);
  }
  .canvas {
    position: relative;
    width: 1200px;
    height: 900px;
  }
  .label {
    position: absolute;
    left: 320px;
    top: 90px;
    width: 560px;
    height: 720px;
    overflow: hidden;
    background: linear-gradient(160deg, var(--label-deep) 0%, var(--label-mid) 55%, var(--label-light) 100%);
    color: var(--ink-light);
    font-family: "Bebas Neue", "Arial Narrow", sans-serif;
    text-align: center;
  }
  .label__foliage {
    position: absolute;
    inset: 0;
    background:
      radial-gradient(ellipse 180px 220px at 40px 140px, rgba(79,169,138,0.45), transparent 70%),
      radial-gradient(ellipse 220px 260px at 500px 320px, rgba(79,169,138,0.5), transparent 70%),
      radial-gradient(ellipse 200px 180px at 90px 640px, rgba(79,169,138,0.4), transparent 70%),
      radial-gradient(ellipse 200px 200px at 470px 640px, rgba(79,169,138,0.45), transparent 70%);
  }
  .brand {
    position: relative;
    margin: 36px auto 0;
    display: inline-flex;
    flex-direction: column;
    align-items: center;
  }
  .brand__row {
    display: flex;
    align-items: center;
    gap: 12px;
  }
  .brand__mark {
    width: 22px;
    height: 22px;
    background: var(--brand-green);
  }
  .brand__name {
    font-size: 72px;
    line-height: 0.9;
    letter-spacing: 4px;
    color: var(--brand-green);
  }
  .brand__tagline {
    font-family: "Open Sans", Arial, sans-serif;
    font-size: 13px;
    color: var(--ink-soft);
    margin-top: 4px;
  }
  .product-name {
    position: relative;
    margin-top: 40px;
    font-size: 74px;
    line-height: 0.95;
    letter-spacing: 1px;
  }
  .product-cbd {
    position: relative;
    margin-top: 10px;
    font-size: 230px;
    line-height: 0.9;
    letter-spacing: 48px;
    padding-left: 48px;
  }
  .product-volume {
    position: relative;
    margin-top: 40px;
    font-size: 30px;
    color: var(--ink-soft);
    letter-spacing: 1px;
  }
  .product-strength {
    position: relative;
    font-size: 18px;
    color: var(--ink-soft);
    letter-spacing: 1px;
  }
</style>
</head>
<body>
  <main class="canvas">
    <section class="label">
      <div class="label__foliage" role="img" aria-label="Soft hemp leaf shapes scattered across the label background"></div>
      <div class="brand">
        <div class="brand__row">
          <span class="brand__mark"></span>
          <span class="brand__name">ULO</span>
        </div>
        <span class="brand__tagline">Quiet Harvest Rituals</span>
      </div>
      <h1 class="product-name">Virgin Organic<br>Hemp Seed Oil</h1>
      <p class="product-cbd">CBD</p>
      <p class="product-volume">10 ML</p>
      <p class="product-strength">CBD 300 MG</p>
    </section>
  </main>
</body>
</html>
```